Business Card Design

We need a business card for a new business based in Sydney, Australia. It is a home based baking business, the key products are cookies and muffins and slices including gluten free baked goods. With the emphasis on home made baking. The target market is cafes, coffee shops and vans, restaurants. Products may be provided in display jars or individually wrapped. The final design should be in the colours pink, purple.

Industry/Entity Type

Business

Contact Information for Business Card

Pindle's Bakery Pty Ltd, Maren Tulloch, maren@pindlesbakery.com.au
0412 506 218, www.pindlesbakery.com.au, ACN 581 246 037,

```html
<!DOCTYPE html>
<html lang="en">
<head>
<meta charset="utf-8">
<title>Pindle's Bakery – Business Card</title>
<link href="https://fonts.googleapis.com/css2?family=Roboto+Condensed:wght@700&family=Questrial&display=swap" rel="stylesheet">
<style>
  :root {
    --page-bg: #efeaee;
    --card-bg: #ffffff;
    --brand-purple: #7a3c9e;
    --brand-pink: #e4579d;
    --deep-purple: #5a2a78;
    --wave-mid: #b0479f;
    --chef-cream: #e9e4b8;
    --chef-brown: #6b5a3e;
  }
  * { margin: 0; padding: 0; box-sizing: border-box; }
  html, body { width: 1200px; height: 800px; overflow: hidden; }
  body {
    background: var(--page-bg);
    display: flex;
    align-items: center;
    justify-content: center;
  }
  .card {
    position: relative;
    width: 1000px;
    height: 600px;
    background: var(--card-bg);
    border-radius: 16px;
    overflow: hidden;
    box-shadow: 0 6px 18px rgba(0,0,0,0.18);
  }
  .chef-illustration {
    position: absolute;
    left: 47px; top: 31px;
    width: 220px; height: 220px;
    border-radius: 50%;
    border: 5px solid var(--chef-brown);
    background: radial-gradient(circle at 45% 40%, #f6f3dc 0%, var(--chef-cream) 70%);
  }
  .chef-watermark {
    position: absolute;
    left: 590px; top: 300px;
    width: 420px; height: 420px;
    border-radius: 50%;
    background: radial-gradient(circle, rgba(233,228,184,0.45) 0%, rgba(233,228,184,0.15) 70%);
  }
  .brand {
    position: absolute;
    left: 360px; top: 48px;
    font-family: "Roboto Condensed", sans-serif;
    font-weight: 700;
    line-height: 1;
  }
  .brand-name {
    display: block;
    color: var(--brand-purple);
    font-size: 118px;
    letter-spacing: 1px;
  }
  .brand-line {
    display: block;
    margin-left: 50px;
    margin-top: 4px;
    white-space: nowrap;
  }
  .brand-trade { color: var(--brand-pink); font-size: 90px; }
  .brand-legal { color: var(--brand-purple); font-size: 48px; margin-left: 6px; }
  .person {
    position: absolute;
    left: 44px; top: 368px;
    font-family: "Roboto Condensed", sans-serif;
    font-weight: 700;
    text-align: right;
    line-height: 1;
  }
  .person-name { color: var(--brand-purple); font-size: 60px; letter-spacing: 0.5px; }
  .person-role { color: var(--brand-pink); font-size: 34px; margin-top: 2px; }
  .contact-list {
    position: absolute;
    left: 600px; top: 358px;
    list-style: none;
    font-family: "Questrial", sans-serif;
    color: var(--deep-purple);
    font-size: 23px;
  }
  .contact-list li { display: flex; align-items: center; gap: 12px; height: 38px; }
  .contact-list svg { width: 24px; height: 24px; fill: var(--brand-pink); flex: none; }
  .footer-wave { position: absolute; left: 0; bottom: 0; width: 1000px; height: 110px; }
  .website {
    position: absolute;
    left: 0; right: 0; bottom: 18px;
    text-align: center;
    font-family: "Questrial", sans-serif;
    color: var(--deep-purple);
    font-size: 25px;
    letter-spacing: 0.5px;
  }
</style>
</head>
<body>
  <article class="card">
    <div class="chef-watermark" role="img" aria-label="Faint chef illustration decoration"></div>
    <div class="chef-illustration" role="img" aria-label="Illustration of a chef rolling dough"></div>

    <h1 class="brand">
      <span class="brand-name">Pindle's</span>
      <span class="brand-line"><span class="brand-trade">BAKERY</span><span class="brand-legal">Pty Ltd,</span></span>
    </h1>

    <div class="person">
      <div class="person-name">MAREN TULLOCH</div>
      <div class="person-role">MANAGER</div>
    </div>

    <ul class="contact-list">
      <li>
        <svg viewBox="0 0 24 24" aria-hidden="true"><path d="M12 2a7 7 0 0 0-7 7c0 5 7 13 7 13s7-8 7-13a7 7 0 0 0-7-7zm0 9.5A2.5 2.5 0 1 1 12 6.5a2.5 2.5 0 0 1 0 5z"/></svg>
        ACN 581 246 037,
      </li>
      <li>
        <svg viewBox="0 0 24 24" aria-hidden="true"><path d="M7 1h10a2 2 0 0 1 2 2v18a2 2 0 0 1-2 2H7a2 2 0 0 1-2-2V3a2 2 0 0 1 2-2zm0 3v14h10V4H7zm5 15.5a1 1 0 1 0 0 2 1 1 0 0 0 0-2z"/></svg>
        0412 506 218
      </li>
      <li>
        <svg viewBox="0 0 24 24" aria-hidden="true"><path d="M2 5h20v14H2V5zm2 2v.5l8 5 8-5V7H4zm0 2.8V17h16V9.8l-8 5-8-5z"/></svg>
        maren@pindlesbakery.com.au
      </li>
    </ul>

    <svg class="footer-wave" viewBox="0 0 1000 110" preserveAspectRatio="none" aria-hidden="true">
      <path d="M0 82 Q460 -50 1000 96 L1000 110 L0 110 Z" fill="var(--brand-purple)"/>
      <path d="M0 90 Q460 -38 1000 100 L1000 110 L0 110 Z" fill="var(--wave-mid)"/>
      <path d="M0 98 Q460 -26 1000 104 L1000 110 L0 110 Z" fill="var(--brand-pink)"/>
    </svg>
    <div class="website">www.pindlesbakery.com.au</div>
  </article>
</body>
</html>
```